Tello Haulage Junk Removal Postcard

I am looking to have a postcard made for my junk removal company. Details:
size: 6"x9"
I would like to keep it clean and simple. Our company colors are pink, blue and white. You can find the colors and info on the company and what we do on our website which is www.tellohaulage.example .
I've attached a sample of a postcard that was made on ArtHive for another junk removal company. I like the way the attached one looks.

```html
<!DOCTYPE html>
<html lang="en">
<head>
<meta charset="utf-8">
<title>Tello Haulage Postcard</title>
<link href="https://fonts.googleapis.com/css2?family=Montserrat:wght@400;500;600;700;800&display=swap" rel="stylesheet">
<style>
  :root {
    --blue: #1c64b0;
    --blue-text: #1d5aa6;
    --pink: #e5098a;
    --pink-dark: #a3066a;
    --white: #ffffff;
    --ink: #333333;
    --page: #e6e7ea;
  }
  * { margin: 0; padding: 0; box-sizing: border-box; }
  html, body { width: 822px; height: 1200px; overflow: hidden; }
  body {
    background: var(--page);
    font-family: "Montserrat", Arial, sans-serif;
    position: relative;
  }
  .card {
    position: absolute;
    left: 83px;
    width: 656px;
    height: 437px;
    background: var(--white);
    overflow: hidden;
  }
  .card--front { top: 117px; }
  .card--back { top: 645px; }
  .shapes { position: absolute; inset: 0; width: 656px; height: 437px; }
  .abs { position: absolute; }

  /* front */
  .brand-name {
    left: 31px; top: 44px;
    font-weight: 800; font-size: 24px; line-height: 1.05;
    color: var(--pink); letter-spacing: -0.5px;
  }
  .service-label {
    left: 235px; top: 29px;
    color: var(--white); font-size: 19px; line-height: 17px; font-weight: 600;
  }
  .service-label b { font-weight: 800; display: block; }
  .service-phone {
    left: 362px; top: 27px;
    color: var(--white); font-size: 37px; font-weight: 800; letter-spacing: -0.5px; line-height: 44px;
  }
  .headline {
    left: 18px; top: 98px;
    color: var(--white); font-size: 32px; line-height: 39px; font-weight: 400;
  }
  .headline b { font-weight: 800; }
  .headline-rule { left: 18px; top: 225px; width: 118px; height: 3px; background: var(--white); }
  .interest {
    left: 18px; top: 238px;
    color: var(--white); font-size: 14.5px; font-weight: 600; line-height: 17px;
  }
  .check-list {
    left: 18px; top: 282px; list-style: none;
    color: var(--white); font-size: 9.3px; line-height: 15.4px;
  }
  .check-list li { display: flex; align-items: center; gap: 2px; }
  .check-list svg { width: 6px; height: 6px; }
  .thumb { top: 315px; width: 54px; height: 54px; border: 1.5px solid var(--white); }
  .thumb--one { left: 153px; background: linear-gradient(180deg, #7fa7d6 0%, #4a6f3c 55%, #3a3a3a 100%); }
  .thumb--two { left: 222px; background: linear-gradient(180deg, #8c9a6a 0%, #c9b79a 50%, #5b5a58 100%); }
  .truck-photo {
    left: 288px; top: 92px; width: 360px; height: 272px;
    background: radial-gradient(ellipse at 45% 55%, #f4f5f7 0%, #d9dce2 45%, rgba(40,40,50,0.85) 80%, rgba(255,255,255,0) 100%);
  }
  .web-front {
    left: 25px; top: 396px;
    color: var(--white); font-size: 20px; font-weight: 500; line-height: 26px;
  }
  .estimate { text-align: right; }
  .estimate-title { font-weight: 800; font-size: 33px; line-height: 34px; letter-spacing: -0.3px; }
  .estimate-sub { font-weight: 600; font-size: 17.5px; line-height: 20px; }
  .estimate--front { right: 24px; top: 374px; }
  .estimate--front .estimate-title { color: var(--pink); }
  .estimate--front .estimate-sub { color: var(--blue-text); }

  /* back */
  .back-headline {
    left: 17px; top: 31px;
    color: var(--white); font-size: 32px; line-height: 36px; font-weight: 400;
  }
  .back-headline b { font-weight: 800; }
  .intro {
    left: 17px; top: 107px; width: 250px;
    color: var(--white); font-size: 12.3px; line-height: 13.5px;
  }
  .task-list {
    left: 17px; top: 165px; list-style: none;
    color: var(--white); font-size: 9.8px; line-height: 16px;
  }
  .task-list li { margin-bottom: 2.3px; }
  .estimate--back { left: 17px; top: 250px; text-align: left; color: var(--white); }
  .brand-name--back { left: 21px; top: 333px; color: var(--white); font-size: 24px; }
  .contact { left: 174px; top: 322px; color: var(--white); }
  .contact-title { font-weight: 800; font-size: 16px; line-height: 20px; }
  .contact-line { font-size: 14px; line-height: 18px; font-weight: 500; }
  .web-back {
    left: 40px; top: 398px;
    color: var(--white); font-size: 20px; font-weight: 500; line-height: 28px;
  }
  .stamp-box { left: 524px; top: 40px; width: 100px; height: 100px; border: 2px solid #444; }
</style>
</head>
<body>

<section class="card card--front">
  <svg class="shapes" viewBox="0 0 656 437" aria-hidden="true">
    <polygon points="232,14 656,14 656,79 212,79" fill="var(--pink)"/>
    <polygon points="0,91 389,91 328,384 0,384" fill="var(--blue)"/>
    <polygon points="346,315 656,315 656,359 337,359" fill="var(--blue)"/>
    <polygon points="0,392 309,392 302,426 0,426" fill="var(--pink)"/>
  </svg>

  <div class="abs brand-name">Tello<br>Haulage</div>
  <div class="abs service-label">CUSTOMER<b>SERVICE</b></div>
  <div class="abs service-phone">555-014-7328</div>

  <h1 class="abs headline"><b>REMOVE</b> THE<br>JUNK <b>RECLAIM</b><br>YOUR SPACE</h1>
  <div class="abs headline-rule"></div>
  <p class="abs interest">Services of Interest - Check<br>All That Apply</p>
  <ul class="abs check-list">
    <li><svg viewBox="0 0 6 6"><rect x="0.3" y="0.3" width="5.4" height="5.4" fill="none" stroke="#fff" stroke-width="0.6"/><path d="M1.2 3 L2.5 4.3 L4.8 1.5" fill="none" stroke="#fff" stroke-width="0.7"/></svg>Residential</li>
    <li><svg viewBox="0 0 6 6"><rect x="0.3" y="0.3" width="5.4" height="5.4" fill="none" stroke="#fff" stroke-width="0.6"/><path d="M1.2 3 L2.5 4.3 L4.8 1.5" fill="none" stroke="#fff" stroke-width="0.7"/></svg>Moving Clean Out</li>
    <li><svg viewBox="0 0 6 6"><rect x="0.3" y="0.3" width="5.4" height="5.4" fill="none" stroke="#fff" stroke-width="0.6"/><path d="M1.2 3 L2.5 4.3 L4.8 1.5" fill="none" stroke="#fff" stroke-width="0.7"/></svg>Downsizing</li>
    <li><svg viewBox="0 0 6 6"><rect x="0.3" y="0.3" width="5.4" height="5.4" fill="none" stroke="#fff" stroke-width="0.6"/><path d="M1.2 3 L2.5 4.3 L4.8 1.5" fill="none" stroke="#fff" stroke-width="0.7"/></svg>Renovation Clean Up</li>
    <li><svg viewBox="0 0 6 6"><rect x="0.3" y="0.3" width="5.4" height="5.4" fill="none" stroke="#fff" stroke-width="0.6"/><path d="M1.2 3 L2.5 4.3 L4.8 1.5" fill="none" stroke="#fff" stroke-width="0.7"/></svg>Commercial</li>
    <li><svg viewBox="0 0 6 6"><rect x="0.3" y="0.3" width="5.4" height="5.4" fill="none" stroke="#fff" stroke-width="0.6"/><path d="M1.2 3 L2.5 4.3 L4.8 1.5" fill="none" stroke="#fff" stroke-width="0.7"/></svg>Something Else. Surprise!</li>
  </ul>
  <div class="abs thumb thumb--one" role="img" aria-label="Photo of the haulage truck parked on a residential street"></div>
  <div class="abs thumb thumb--two" role="img" aria-label="Photo of junk and furniture piled in front of a garage"></div>
  <div class="abs truck-photo" role="img" aria-label="Photo of the white company dump truck with a crew member standing beside it"></div>

  <div class="abs web-front">www.tellohaulage.example</div>
  <div class="abs estimate estimate--front">
    <div class="estimate-title">FREE ESTIMATE</div>
    <div class="estimate-sub">Provided prior to item removal</div>
  </div>
</section>

<section class="card card--back">
  <svg class="shapes" viewBox="0 0 656 437" aria-hidden="true">
    <polygon points="290,0 300,0 397,437 385,437" fill="var(--pink)"/>
    <polygon points="0,0 290,0 385,437 0,437" fill="var(--blue)"/>
    <polygon points="0,312 375,312 400,390 0,390" fill="var(--pink)"/>
    <polygon points="378,390 400,390 382,405" fill="var(--pink-dark)"/>
    <polygon points="0,390 372,390 380,437 0,437" fill="var(--blue)"/>
    <g stroke="#555" stroke-width="1" stroke-dasharray="3 4">
      <line x1="373" y1="209" x2="625" y2="209"/>
      <line x1="387" y1="251" x2="625" y2="251"/>
      <line x1="395" y1="292" x2="625" y2="292"/>
      <line x1="402" y1="333" x2="625" y2="333"/>
      <line x1="410" y1="375" x2="625" y2="375"/>
    </g>
  </svg>

  <h2 class="abs back-headline"><b>RELAX, WE DO</b><br>THE DIRTY WORK</h2>
  <p class="abs intro">We're more than just junk. Capitalizing on our years of experience we can work directly with you on a multitude of projects around your house:</p>
  <ul class="abs task-list">
    <li>• Packing and prepping for your move</li>
    <li>• Loading/unloading your rental truck or POD</li>
    <li>• Donation pickup</li>
    <li>• Mulch, gravel and topsoil delivery</li>
  </ul>
  <div class="abs estimate estimate--back">
    <div class="estimate-title">FREE ESTIMATE</div>
    <div class="estimate-sub">Provided prior to item removal</div>
  </div>

  <div class="abs brand-name brand-name--back">Tello<br>Haulage</div>
  <div class="abs contact">
    <div class="contact-title">CONTACT</div>
    <div class="contact-line">555-014-7328</div>
    <div class="contact-line">info@tellohaulage.example</div>
  </div>
  <div class="abs web-back">www.tellohaulage.example</div>

  <div class="abs stamp-box"></div>
</section>

</body>
</html>
```